Safety Work Area Signage to keep people away from work zone

We would like to create a simple design that will include our logo and phone number, 'work area', and 'caution / cuidado' (please see a mock-up of the intended design in the uploaded files). Please provide multiple options. We would like a Professional look for the poster as it is meant for safety. Poster Size to be: 18.16" X 23.10"

Target Market(s)

General Public on Construction Sites

Font styles to use
Serif

Requirements
Must have
• see mock-ups in uploaded files
Nice to have
• Simple Design, Professional Look

```html
<!DOCTYPE html>
<html lang="en">
<head>
<meta charset="utf-8">
<title>Work Area Safety Sign</title>
<link rel="stylesheet" href="https://fonts.googleapis.com/css2?family=Merriweather:wght@700;900&display=swap">
<style>
  :root {
    --sign-red: #be1e2d;
    --sign-blue: #2e3192;
    --name-blue: #1f2191;
    --sign-white: #ffffff;
  }
  html, body {
    margin: 0;
    padding: 0;
    width: 921px;
    height: 1200px;
    overflow: hidden;
    background: var(--sign-white);
  }
  .sign {
    display: block;
    width: 921px;
    height: 1200px;
  }
  .hazard-stripe { fill: var(--sign-red); }
  .caution-bar { fill: var(--sign-blue); }
  .caution-label {
    font-family: "Merriweather", Georgia, serif;
    font-weight: 900;
    font-size: 54px;
    fill: var(--sign-white);
  }
  .warning-triangle {
    fill: var(--sign-red);
    stroke: var(--sign-white);
    stroke-width: 10;
    stroke-linejoin: round;
  }
  .warning-mark { fill: var(--sign-white); }
  .headline {
    font-family: "Merriweather", Georgia, serif;
    font-weight: 900;
    font-size: 250px;
    fill: var(--sign-red);
  }
  .company-name {
    font-family: "Merriweather", Georgia, serif;
    font-weight: 900;
    fill: var(--name-blue);
  }
  .company-divider {
    stroke: var(--name-blue);
    stroke-width: 3;
  }
  .company-trade {
    font-family: "Merriweather", Georgia, serif;
    font-weight: 900;
    font-size: 46px;
    fill: var(--name-blue);
  }
  .tagline {
    font-family: "Merriweather", Georgia, serif;
    font-weight: 900;
    font-size: 36px;
    fill: var(--name-blue);
  }
  .phone {
    font-family: "Merriweather", Georgia, serif;
    font-weight: 900;
    font-size: 86px;
    fill: var(--sign-blue);
  }
</style>
</head>
<body>
<svg class="sign" viewBox="0 0 921 1200" xmlns="http://www.w3.org/2000/svg" role="img" aria-label="Caution, Cuidado: Work Area. Harlow and Co., Inc., General Contractors. We Build Lasting Trust. (407) 555-0148">
  <defs>
    <pattern id="hazard-pattern" width="72" height="60" patternUnits="userSpaceOnUse" patternTransform="skewX(-38)">
      <rect class="hazard-stripe" x="0" y="0" width="40" height="60"/>
    </pattern>
  </defs>

  <!-- top hazard band -->
  <rect class="hazard-band" x="22" y="16" width="878" height="60" fill="url(#hazard-pattern)"/>

  <!-- caution banner -->
  <rect class="caution-bar" x="62" y="132" width="798" height="110"/>
  <text class="caution-label" x="62" y="208" dx="14" textLength="280" lengthAdjust="spacingAndGlyphs">CAUTION</text>
  <text class="caution-label" x="846" y="208" text-anchor="end" textLength="280" lengthAdjust="spacingAndGlyphs">CUIDADO</text>

  <g class="warning-icon">
    <path class="warning-triangle" d="M460 96 L560 270 L360 270 Z"/>
    <path class="warning-mark" d="M449 132 Q460 122 471 132 L467 218 Q460 226 453 218 Z"/>
    <circle class="warning-mark" cx="460" cy="246" r="12"/>
  </g>

  <!-- headline -->
  <text class="headline" x="58" y="493" textLength="802" lengthAdjust="spacingAndGlyphs">WORK</text>
  <text class="headline" x="58" y="721" textLength="802" lengthAdjust="spacingAndGlyphs">AREA</text>

  <!-- company block -->
  <text class="company-name" x="108" y="846" font-size="62" textLength="316" lengthAdjust="spacingAndGlyphs">Harlow</text>
  <text class="company-name" x="108" y="892" font-size="34" textLength="316" lengthAdjust="spacingAndGlyphs">&amp; Co., Inc.</text>
  <line class="company-divider" x1="452" y1="786" x2="452" y2="906"/>
  <text class="company-trade" x="649" y="838" text-anchor="middle" textLength="250" lengthAdjust="spacingAndGlyphs">General</text>
  <text class="company-trade" x="649" y="892" text-anchor="middle" textLength="326" lengthAdjust="spacingAndGlyphs">Contractors</text>

  <text class="tagline" x="460" y="957" text-anchor="middle" textLength="660" lengthAdjust="spacingAndGlyphs">“We Build Lasting Trust”</text>

  <text class="phone" x="460" y="1083" text-anchor="middle" textLength="668" lengthAdjust="spacingAndGlyphs">(407) 555-0148</text>

  <!-- bottom hazard band -->
  <rect class="hazard-band" x="22" y="1124" width="878" height="58" fill="url(#hazard-pattern)"/>
</svg>
</body>
</html>
```